Full Page Appliance Ad

Create a full page ad (7.5" W x 10" H) representing that we are a full service appliance company, where we have a showroom located at 14 N. Birch Lane Marrowfield, PA 18970. Our website is www.qrtolvek.com , and our phone number is 215-555-0148. We don't only sell appliances, we deliver, install, and service. We also offer an additional year warranty* (see store for details). In addition to appliances, we also have an Electrical Department that specializes in residential applications.
May be best if split the full page ad into two spots. One spot to reference appliances, and the other to represent electrical.
I want it to look clean, and not too busy
Target Market(s)
30-70 years old
Look and feel

```html
<!DOCTYPE html>
<html lang="en">
<head>
<meta charset="utf-8">
<title>Qrtolvek and Son Inc – Appliances &amp; Electrical</title>
<link href="https://fonts.googleapis.com/css2?family=Montserrat:wght@400;700&family=Open+Sans:wght@400;800&family=Source+Sans+3:wght@400;600;700&display=swap" rel="stylesheet">
<style>
  :root {
    --ink: #1a1a1a;
    --navy: #1c1c3a;
    --grey-text: #707070;
    --grey-strong: #6a6a6a;
    --band: #6e6e6e;
    --band-dark: #222222;
    --footer: #dcdcdc;
    --white: #ffffff;
    --hero-light: #a6a6a6;
    --hero-mid: #8a8a8a;
    --hero-floor: #cfcfcf;
  }
  * { margin: 0; padding: 0; box-sizing: border-box; }
  html, body { width: 900px; height: 1200px; overflow: hidden; background: var(--white); }
  .ad { position: relative; width: 900px; height: 1200px; overflow: hidden; background: var(--white); font-family: "Source Sans 3", sans-serif; color: var(--ink); }

  .hero { position: absolute; left: 0; top: 0; width: 900px; height: 527px;
    background: linear-gradient(180deg, var(--hero-light) 0%, var(--hero-mid) 70%, var(--hero-floor) 100%); }
  .hero-headline { position: absolute; left: 514px; top: 88px; color: var(--white); font-family: "Open Sans", sans-serif; font-weight: 800; }
  .hero-kicker { font-size: 18px; letter-spacing: -0.2px; line-height: 22px; }
  .hero-title { font-size: 40px; line-height: 41px; letter-spacing: -0.4px; margin-top: 4px; }

  .showroom { position: absolute; left: 0; top: 566px; width: 900px; text-align: center; font-family: "Montserrat", sans-serif; font-weight: 400; font-size: 39px; line-height: 41px; color: var(--grey-text); letter-spacing: 0.3px; }
  .showroom strong { font-weight: 700; color: var(--grey-strong); }

  .services { position: absolute; left: 0; top: 720px; width: 900px; text-align: center; font-size: 17.5px; line-height: 24px; color: var(--ink); }

  .warranty { position: absolute; left: 182px; top: 789px; width: 549px; height: 120px; }
  .warranty svg { position: absolute; left: 0; top: 0; }
  .warranty-text { position: absolute; left: 9px; top: 22px; width: 532px; text-align: center; color: var(--white); font-size: 16.5px; line-height: 24px; }
  .warranty-title { font-weight: 700; font-size: 17px; }

  .feature { position: absolute; top: 957px; display: flex; align-items: center; gap: 12px; font-size: 19px; line-height: 24px; color: var(--ink); }
  .feature--residential { left: 182px; }
  .feature--specialty { left: 470px; }

  .footer { position: absolute; left: 0; top: 1040px; width: 900px; height: 135px; background: var(--footer); }
  .brand { position: absolute; left: 90px; top: 35px; display: flex; align-items: center; gap: 14px; }
  .brand-mark { width: 44px; height: 44px; border-radius: 50%; background: var(--navy); flex: none; }
  .brand-name { font-family: "Source Sans 3", sans-serif; font-weight: 700; font-size: 30px; color: var(--navy); line-height: 32px; }
  .contact { position: absolute; left: 463px; top: 18px; list-style: none; font-size: 18px; line-height: 24px; color: var(--ink); }
  .contact li { display: flex; align-items: flex-start; gap: 10px; }
  .contact svg { flex: none; margin-top: 5px; }
  .contact .indent { padding-left: 24px; }
</style>
</head>
<body>
<div class="ad">
  <section class="hero" role="img" aria-label="Photo-style scene of home appliances on a tiled floor: refrigerator, wall air conditioner, microwave over a wall oven, front-load washer and canister vacuum">
    <div class="hero-headline">
      <div class="hero-kicker">YOUR ONE-STOP SHOP FOR</div>
      <div class="hero-title">ALL APPLIANCE<br>NEEDS!</div>
    </div>
  </section>

  <h1 class="showroom">VISIT OUR SHOWROOM<br>EXPLORE A <strong>WIDE RANGE</strong> OF<br>APPLIANCES IN PERSON.</h1>

  <p class="services">Sales, Delivery, Installation, and Service:<br>We handle everything from start to finish.</p>

  <div class="warranty">
    <svg width="549" height="120" viewBox="0 0 549 120" aria-hidden="true">
      <rect x="9" y="10" width="532" height="101" fill="var(--band)"/>
      <polygon points="0,0 75,0 0,79" fill="var(--band-dark)"/>
      <polygon points="549,41 549,120 474,120" fill="var(--band-dark)"/>
    </svg>
    <div class="warranty-text">
      <div class="warranty-title">ADDITIONAL YEAR WARRANTY</div>
      <div>Enjoy peace of mind with our extended warranty*<br>(see store for details).</div>
    </div>
  </div>

  <div class="feature feature--residential">
    <svg width="46" height="46" viewBox="0 0 46 46" aria-hidden="true" fill="none" stroke="var(--ink)" stroke-width="3" stroke-linejoin="round">
      <path d="M3 22 L23 4 L43 22"/>
      <path d="M9 17 V43 H37 V17"/>
      <path d="M18 22 V27 M28 22 V27 M15 27 H31 V31 A8 8 0 0 1 15 31 Z M23 38 V43"/>
    </svg>
    <span>Expert Residential<br>Electrical Services!</span>
  </div>

  <div class="feature feature--specialty">
    <svg width="44" height="46" viewBox="0 0 44 46" aria-hidden="true" fill="none" stroke="var(--ink)" stroke-width="2" stroke-linecap="round" stroke-linejoin="round">
      <path d="M22 8 A9 9 0 0 1 27 24 V28 H17 V24 A9 9 0 0 1 22 8 Z"/>
      <path d="M18 31 H26 M23 13 L20 18 H24 L21 23"/>
      <path d="M22 2 V4 M10 8 L12 10 M34 8 L32 10 M6 17 H8 M36 17 H38"/>
      <path d="M3 26 V36 L11 44 H19 V38 L12 32 M41 26 V36 L33 44 H25 V38 L32 32"/>
    </svg>
    <span>Specializing in All Your<br>Home Electrical Needs</span>
  </div>

  <footer class="footer">
    <div class="brand">
      <span class="brand-mark" aria-hidden="true"></span>
      <span class="brand-name">QRTOLVEK<br>AND SON INC</span>
    </div>
    <ul class="contact">
      <li>
        <svg width="14" height="16" viewBox="0 0 14 16" aria-hidden="true"><path d="M7 1 A5.5 5.5 0 0 1 12.5 6.5 C12.5 10 7 15 7 15 C7 15 1.5 10 1.5 6.5 A5.5 5.5 0 0 1 7 1 Z" fill="var(--ink)"/><circle cx="7" cy="6.5" r="2" fill="var(--footer)"/></svg>
        <span>Located at 14 N. Birch Lane Marrowfield,</span>
      </li>
      <li class="indent">PA 18970</li>
      <li>
        <svg width="14" height="14" viewBox="0 0 14 14" aria-hidden="true" fill="none" stroke="var(--ink)" stroke-width="1.3"><circle cx="7" cy="7" r="6"/><ellipse cx="7" cy="7" rx="2.6" ry="6"/><path d="M1 7 H13 M2 4 H12 M2 10 H12"/></svg>
        <span>www.qrtolvek.com</span>
      </li>
      <li>
        <svg width="14" height="14" viewBox="0 0 14 14" aria-hidden="true"><circle cx="7" cy="7" r="6.2" fill="none" stroke="var(--ink)" stroke-width="1.3"/><path d="M4.5 3.8 L6 3.6 L6.6 5.6 L5.7 6.3 C6.1 7.2 6.8 7.9 7.7 8.3 L8.4 7.4 L10.4 8 L10.2 9.5 C7 9.8 4.2 7 4.5 3.8 Z" fill="var(--ink)"/></svg>
        <span>215-555-0148</span>
      </li>
    </ul>
  </footer>
</div>
</body>
</html>
```